Business Card Design Project

Doctor, Pain Management. Need a new business card design with appointment info on the back. New address is 18 Birchwood Court, Suite 304, Holloway, NJ 07519. Right now I believe the rest of the information is staying the same.

```html
<!DOCTYPE html>
<html lang="en">
<head>
<meta charset="utf-8">
<title>ReliefPoint Pain Management – Business Card</title>
<link rel="stylesheet" href="https://fonts.googleapis.com/css2?family=Poppins:wght@400;500;600&family=Tinos:wght@700&display=swap">
<style>
  :root {
    --page: #d9d9d9;
    --ink-dark: #322f26;
    --cream: #f0e5d9;
    --taupe: #b2a597;
    --paper: #f6f5f2;
    --yellow: #eee52b;
    --text: #1f1d19;
    --rule: #8a8a86;
    --sans: "Poppins", sans-serif;
    --serif: "Tinos", serif;
  }
  * { box-sizing: border-box; margin: 0; padding: 0; }
  html, body { width: 1200px; height: 1200px; overflow: hidden; }
  body {
    background: var(--page);
    font-family: var(--sans);
    display: flex;
    flex-direction: column;
    align-items: center;
    justify-content: center;
    gap: 44px;
  }
  .card {
    position: relative;
    width: 900px;
    height: 514px;
    overflow: hidden;
    box-shadow: 0 6px 18px rgba(0,0,0,.18);
  }

  /* Front */
  .card-front { background: var(--cream); }
  .card-front .wave { position: absolute; inset: 0; width: 100%; height: 100%; }
  .brand {
    position: absolute;
    left: 60px;
    top: 250px;
    width: 330px;
    display: flex;
    flex-direction: column;
    align-items: center;
    color: var(--yellow);
    font-weight: 500;
  }
  .brand-mark {
    width: 70px; height: 70px;
    border-radius: 50%;
    background: var(--yellow);
    margin-bottom: 22px;
  }
  .brand-name { font-size: 40px; line-height: 1.05; }
  .brand-sub { font-size: 30px; line-height: 1.2; }

  .doctor {
    position: absolute;
    right: 52px;
    top: 52px;
    text-align: right;
    color: var(--text);
  }
  .doctor-name {
    font-family: var(--serif);
    font-size: 42px;
    letter-spacing: .5px;
  }
  .doctor-name small { font-size: 22px; }
  .doctor-title { font-size: 19px; margin-top: 2px; }

  .contact {
    position: absolute;
    right: 52px;
    top: 196px;
    text-align: right;
    font-size: 17px;
    line-height: 1.55;
    color: var(--text);
  }
  .contact b { font-weight: 600; }
  .contact .gap { height: 22px; }

  /* Back */
  .card-back { background: var(--paper); }
  .band {
    position: absolute;
    left: 0; right: 0;
    background: var(--ink-dark);
  }
  .band-top { top: 0; height: 138px; display: flex; align-items: flex-end; justify-content: center; padding-bottom: 20px; }
  .band-top h2 { color: var(--yellow); font-size: 44px; font-weight: 600; letter-spacing: 1px; }
  .band-bottom {
    bottom: 0; height: 150px;
    color: #fff;
    font-size: 22px;
    display: flex; flex-direction: column; justify-content: center; align-items: center;
    gap: 6px;
  }
  .band-bottom .label { color: var(--yellow); }
  .band-bottom .sep { margin: 0 14px; }

  .form { position: absolute; left: 60px; right: 60px; top: 158px; }
  .field { display: flex; align-items: flex-end; gap: 10px; font-size: 22px; font-weight: 600; color: var(--text); }
  .field .line { flex: 1; border-bottom: 1.5px solid var(--rule); height: 24px; }
  .days { display: flex; justify-content: space-between; margin: 22px 0 26px 70px; }
  .day { display: flex; align-items: center; gap: 10px; font-size: 19px; font-weight: 500; color: var(--text); }
  .box { width: 26px; height: 26px; border: 2px solid var(--text); background: #fff; }
  .note { font-size: 14px; color: var(--text); margin: 8px 0 0 80px; }
</style>
</head>
<body>

<section class="card card-front" aria-label="Business card front">
  <svg class="wave" viewBox="0 0 900 514" preserveAspectRatio="none" aria-hidden="true">
    <path d="M150,0 C320,40 380,380 560,514 L610,514 C420,370 360,25 195,0 Z" fill="var(--taupe)"/>
    <path d="M0,0 L150,0 C320,40 380,380 560,514 L0,514 Z" fill="var(--ink-dark)"/>
  </svg>

  <div class="brand">
    <span class="brand-mark"></span>
    <span class="brand-name">ReliefPoint</span>
    <span class="brand-sub">Pain Management</span>
  </div>

  <div class="doctor">
    <h1 class="doctor-name">LENA VOSS<small>, M.D., Ph.D</small></h1>
    <p class="doctor-title">Board Certified Anesthesiologist</p>
  </div>

  <div class="contact">
    <p><b>P:</b> 555.014.2290</p>
    <p><b>F:</b> 555.014.2291</p>
    <div class="gap"></div>
    <p>18 Birchwood Court, Suite 304</p>
    <p>Holloway, NJ 07519</p>
    <div class="gap"></div>
    <p><b>E:</b> frontdesk@reliefpointclinic.com</p>
    <p><b>W:</b> www.reliefpointclinic.com</p>
  </div>
</section>

<section class="card card-back" aria-label="Business card back">
  <div class="band band-top"><h2>Appointment</h2></div>

  <div class="form">
    <div class="field"><span>For:</span><span class="line"></span></div>
    <div class="days">
      <span class="day"><span class="box"></span>Mon</span>
      <span class="day"><span class="box"></span>Tue</span>
      <span class="day"><span class="box"></span>Wed</span>
      <span class="day"><span class="box"></span>Thu</span>
      <span class="day"><span class="box"></span>Fri</span>
      <span class="day"><span class="box"></span>Sat</span>
      <span class="day"><span class="box"></span>Sun</span>
    </div>
    <div class="field"><span>Date:</span><span class="line"></span></div>
    <p class="note">if you are unable to keep your appointment, please contact us as soon as possible</p>
  </div>

  <div class="band band-bottom">
    <p><span class="label">P:</span> 555.014.2290<span class="sep">|</span><span class="label">F:</span> 555.014.2291</p>
    <p><span class="label">E:</span> frontdesk@reliefpointclinic.com<span class="sep">|</span><span class="label">W:</span> reliefpointclinic.com</p>
  </div>
</section>

</body>
</html>
```